Rancho Brisolo Wine Bottle Label

Hello! We are looking for a wine bottle label design for our private, family winery located in Chico, CA. The name of our home/ranch/vineyard is Rancho Brisolo ('the exit'), which is inspired by our hilltop location, panoramic views of the valley, and sensation of escaping from the busy world below.

We planted our vineyard in 2011 and are now bottling our first harvest from fall of 2013. We planted all Italian varietals on our land: syrah, primitivo, and montepulciano. The wine we make is the culmination of all the love, support and effort poured into the process by our family and friends.

The task at hand: we are looking for a clean, simple front and back wine label design.

Front Label Content:
RB and/or Rancho Brisolo
Estate Grown
Chico, CA
Varietal (use Syrah for placeholder)
Year (use 2013 for placeholder)

Back Label Content:
Running list of names of all family and friends who have participated in the process (use a text fill for placeholder)

Aesthetic Description:
Simple, clean, contemporary, text based design (see attached logo idea, Image #1)
Like the brown paper with stamped lettering look & feel
Like the classic clear label with gold lettering look & feel
Option to incorporated a simple background image/sketch of the view overlooking the valley (see attached Image #2 and #3)
Additional inspirational images attached for reference (Images #3- )

General Size Requirement:
Front Label - 4"tall by 3 1/2" wide
Back Label - 4"tall by 3 1/2" wide

Format:
Please submit Photoshop or Illustrator or InDesign Files and PDF/EPS Files.

Industry/Entity Type

Ranch

```html
<!DOCTYPE html>
<html lang="en">
<head>
<meta charset="utf-8">
<title>Rancho Brisolo – Back Label</title>
<link href="https://fonts.googleapis.com/css2?family=Questrial&family=Abel&display=swap" rel="stylesheet">
<style>
  :root {
    --ink: #111111;
    --wine: #c1272d;
    --spot-red: #8c2633;
    --label-edge: #8f8f8f;
    --paper: #ffffff;
  }
  html, body {
    margin: 0;
    padding: 0;
    width: 1200px;
    height: 900px;
    overflow: hidden;
    background: var(--paper);
  }
  .canvas {
    position: relative;
    width: 1200px;
    height: 900px;
    font-family: "Questrial", "Helvetica Neue", Arial, sans-serif;
    color: var(--ink);
  }
  .back-label {
    position: absolute;
    left: 348px;
    top: 105px;
    width: 526px;
    height: 601px;
    border: 1px solid var(--label-edge);
    border-radius: 5px;
    box-sizing: border-box;
  }
  .brand {
    position: absolute;
    left: 24px;
    top: 100px;
    width: 216px;
    display: flex;
    align-items: center;
    justify-content: center;
    gap: 8px;
  }
  .brand-dot {
    width: 10px;
    height: 10px;
    border-radius: 50%;
    background: var(--ink);
  }
  .brand-name {
    font-size: 20px;
    color: var(--ink);
    white-space: nowrap;
  }
  .wine-title {
    position: absolute;
    left: 24px;
    top: 166px;
    width: 216px;
    text-align: center;
    line-height: 1;
  }
  .varietal { font-size: 24px; letter-spacing: 1.5px; -webkit-text-stroke: 0.3px var(--ink); }
  .vintage { font-size: 21px; margin-top: 3px; letter-spacing: 0.8px; }
  .wine-style { font-size: 16px; color: var(--wine); margin-top: 4px; letter-spacing: 1px; -webkit-text-stroke: 0.3px var(--wine); }
  .producer {
    position: absolute;
    left: 25px;
    top: 314px;
    font-size: 15px;
    line-height: 17.5px;
    letter-spacing: 0.4px;
  }
  .compliance {
    position: absolute;
    left: 24px;
    top: 428px;
    width: 220px;
  }
  .symbols { display: flex; align-items: center; gap: 6px; }
  .symbols svg { display: block; }
  .sulphites {
    font-size: 12.5px;
    line-height: 15px;
    margin-left: 10px;
    margin-top: -6px;
  }
  .volume {
    display: flex;
    align-items: center;
    font-size: 20px;
    margin-top: 5px;
    letter-spacing: 0.3px;
  }
  .volume .estimate { font-size: 24px; margin-right: 2px; line-height: 1; }
  .volume .abv { margin-left: 24px; }
  .barcode-slot {
    position: absolute;
    left: 24px;
    top: 497px;
    width: 216px;
    height: 80px;
    border: 2px solid var(--ink);
    box-sizing: border-box;
    font-size: 19px;
    display: flex;
    align-items: center;
    justify-content: center;
    padding-right: 14px;
    letter-spacing: 0.6px;
  }
  .supporters {
    position: absolute;
    left: 263px;
    top: 35px;
    margin: 0;
    padding: 0;
    list-style: none;
    font-family: "Abel", "Arial Narrow", sans-serif;
    font-size: 17.5px;
    line-height: 20px;
    white-space: nowrap;
    letter-spacing: 0.45px;
    -webkit-text-stroke: 0.35px var(--ink);
  }
  .spec {
    position: absolute;
    left: 351px;
    top: 719px;
    font-size: 20px;
    line-height: 24px;
    letter-spacing: 1px;
    -webkit-text-stroke: 0.4px var(--ink);
  }
  .swatches {
    position: absolute;
    left: 350px;
    top: 777px;
    font-size: 16.5px;
    letter-spacing: 1px;
  }
  .swatch-row { display: flex; align-items: center; height: 24px; }
  .chip { width: 21px; height: 21px; margin-right: 14px; }
  .chip-black { background: #000; }
  .chip-spot { background: var(--spot-red); }
  .swatch-spot { color: var(--spot-red); }
</style>
</head>
<body>
<div class="canvas">
  <section class="back-label">
    <div class="brand">
      <span class="brand-dot"></span>
      <span class="brand-name">Rancho Brisolo</span>
    </div>

    <div class="wine-title">
      <div class="varietal">SYRAH</div>
      <div class="vintage">2013</div>
      <div class="wine-style">RED DRY WINE</div>
    </div>

    <div class="producer">
      Produced and bottled by<br>
      RANCHO BRISOLO WINERY<br>
      Adress:<br>
      phone:<br>
      www.ranchobrisolo.com
    </div>

    <div class="compliance">
      <div class="symbols">
        <svg width="30" height="30" viewBox="0 0 30 30" role="img" aria-label="Pregnancy warning symbol">
          <circle cx="15" cy="15" r="13" fill="none" stroke="#111" stroke-width="2.5"/>
          <line x1="6" y1="6" x2="24" y2="24" stroke="#111" stroke-width="2.5"/>
        </svg>
        <svg width="24" height="28" viewBox="0 0 24 28" role="img" aria-label="Dispose in bin symbol">
          <rect x="9" y="12" width="11" height="14" fill="none" stroke="#111" stroke-width="2"/>
          <line x1="7" y1="11" x2="22" y2="11" stroke="#111" stroke-width="2"/>
        </svg>
        <svg width="26" height="28" viewBox="0 0 26 28" role="img" aria-label="Recycle glass symbol">
          <path d="M13 4 L22 19 L4 19 Z" fill="none" stroke="#111" stroke-width="2.5"/>
        </svg>
        <div class="sulphites">contains<br>sulphites</div>
      </div>
      <div class="volume">
        <span class="estimate">&#8494;</span>750ml
        <span class="abv">Alc12.5%vol</span>
      </div>
    </div>

    <div class="barcode-slot">bar code</div>

    <ul class="supporters">
      <li>NAME SURNAME NAME SURNAME</li>
      <li>NAME SURNAME NAME SURNAME</li>
      <li>NAME SURNAME NAME SURNAME</li>
      <li>NAME SURNAME NAME SURNAME</li>
      <li>NAME SURNAME NAME SURNAME</li>
      <li>NAME SURNAME NAME SURNAME</li>
      <li>NAME SURNAME NAME SURNAME</li>
      <li>NAME SURNAME NAME SURNAME</li>
      <li>NAME SURNAME NAME SURNAME</li>
      <li>NAME SURNAME NAME SURNAME</li>
      <li>NAME SURNAME NAME SURNAME</li>
      <li>NAME SURNAME NAME SURNAME</li>
      <li>NAME SURNAME NAME SURNAME</li>
      <li>NAME SURNAME NAME SURNAME</li>
      <li>NAME SURNAME NAME SURNAME</li>
      <li>NAME SURNAME NAME SURNAME</li>
      <li>NAME SURNAME NAME SURNAME</li>
      <li>NAME SURNAME NAME SURNAME</li>
      <li>NAME SURNAME NAME SURNAME</li>
      <li>NAME SURNAME NAME SURNAME</li>
      <li>NAME SURNAME NAME SURNAME</li>
      <li>NAME SURNAME NAME SURNAME</li>
      <li>NAME SURNAME NAME SURNAME</li>
      <li>NAME SURNAME NAME SURNAME</li>
      <li>NAME SURNAME NAME SURNAME</li>
      <li>NAME SURNAME NAME SURNAME</li>
      <li>NAME SURNAME NAME SURNAME</li>
    </ul>
  </section>

  <div class="spec">
    BACK LABEL<br>
    size - 4x3,5 in
  </div>

  <div class="swatches">
    <div class="swatch-row"><span class="chip chip-black"></span>100% Black</div>
    <div class="swatch-row swatch-spot"><span class="chip chip-spot"></span>SPOT RED 202C</div>
  </div>
</div>
</body>
</html>
```